Modern Design Business Card industrial maintenance company

Business card design for Company named Brookvale Equipment Services

Target Market(s)

Industrial

Industry/Entity Type

Maintenance and repair

Contact Information for Business Card

Place holder for address, office phone, mobile number and email

Requirements
Must have
• Clean modern look
Nice to have
• N/a

```html
<!DOCTYPE html>
<html lang="en">
<head>
<meta charset="utf-8">
<title>Brookvale Equipment Services – Business Card</title>
<link rel="stylesheet" href="https://fonts.googleapis.com/css2?family=Michroma&family=Poppins:wght@400;500&display=swap">
<style>
  :root {
    --bg: #7a7a80;
    --card-white: #ffffff;
    --card-black: #0b0b0b;
    --ink: #161616;
    --ink-soft: #2a2a2a;
    --rule: #3a3a3a;
    --faint: #dcdcdc;
    --paper-ink: #ffffff;
  }
  * { box-sizing: border-box; margin: 0; padding: 0; }
  html, body { width: 1200px; height: 900px; overflow: hidden; }
  body {
    background: var(--bg);
    display: flex;
    align-items: center;
    justify-content: center;
    gap: 50px;
    font-family: "Poppins", sans-serif;
  }
  .card {
    position: relative;
    width: 540px;
    height: 309px;
    border-radius: 16px;
    overflow: hidden;
  }
  .card--front { background: var(--card-white); color: var(--ink); }
  .card--back { background: var(--card-black); color: var(--paper-ink); }

  .faint-mark {
    position: absolute;
    right: 40px;
    top: -60px;
    width: 220px;
    height: 220px;
    border: 9px solid var(--faint);
    border-radius: 50%;
  }
  .brand {
    position: absolute;
    display: flex;
    align-items: center;
    gap: 12px;
  }
  .brand__dot {
    width: 40px; height: 40px;
    border: 3px solid currentColor;
    border-radius: 50%;
    flex: none;
  }
  .brand__name {
    font-family: "Michroma", sans-serif;
    font-size: 13px;
    letter-spacing: 0.06em;
    text-transform: uppercase;
    line-height: 1.35;
  }
  .card--front .brand { left: 28px; top: 38px; }

  .person { position: absolute; left: 28px; top: 142px; }
  .person__name {
    font-family: "Michroma", sans-serif;
    font-size: 19px;
    letter-spacing: 0.08em;
  }
  .person__role {
    font-family: "Michroma", sans-serif;
    font-size: 11px;
    letter-spacing: 0.14em;
    margin-top: 6px;
  }
  .divider {
    position: absolute;
    left: 28px; right: 28px; top: 200px;
    height: 1px;
    background: var(--rule);
  }
  .contacts {
    position: absolute;
    left: 28px; top: 214px;
    list-style: none;
    font-size: 15px;
    line-height: 1.45;
    color: var(--ink-soft);
  }
  .contacts li { display: flex; align-items: center; gap: 10px; }
  .contacts svg { width: 13px; height: 13px; flex: none; }
  .address {
    position: absolute;
    right: 28px; top: 214px;
    text-align: right;
    font-size: 14px;
    line-height: 1.45;
    color: var(--ink-soft);
  }

  .card--back .brand {
    left: 0; right: 0; top: 0; bottom: 0;
    flex-direction: column;
    justify-content: center;
    gap: 18px;
  }
  .card--back .brand__dot { width: 92px; height: 92px; border-width: 4px; }
  .card--back .brand__name { font-size: 20px; text-align: center; }
</style>
</head>
<body>
  <section class="card card--front" aria-label="Business card front">
    <div class="faint-mark" aria-hidden="true"></div>
    <div class="brand">
      <span class="brand__dot"></span>
      <span class="brand__name">Brookvale<br>Equipment Services</span>
    </div>
    <div class="person">
      <p class="person__name">DANIEL REYES</p>
      <p class="person__role">CEO/FOUNDER</p>
    </div>
    <div class="divider"></div>
    <ul class="contacts">
      <li>
        <svg viewBox="0 0 16 16" aria-hidden="true"><path d="M4 1l3 3-2 2c1 2 3 4 5 5l2-2 3 3-2 3C7 15 1 9 1 3z" fill="currentColor"/></svg>
        316-555-0184
      </li>
      <li>
        <svg viewBox="0 0 16 16" aria-hidden="true"><rect x="4" y="1" width="8" height="14" rx="1.5" fill="none" stroke="currentColor" stroke-width="1.6"/></svg>
        316-555-0184
      </li>
      <li>
        <svg viewBox="0 0 16 16" aria-hidden="true"><rect x="1" y="3" width="14" height="10" fill="currentColor"/><path d="M1 3l7 6 7-6" fill="none" stroke="#fff" stroke-width="1.2"/></svg>
        daniel@brookvalemail.com
      </li>
    </ul>
    <p class="address">P.O. Box 417 3290 Alder Rd<br>Milford Kansas 60412</p>
  </section>

  <section class="card card--back" aria-label="Business card back">
    <div class="brand">
      <span class="brand__dot"></span>
      <span class="brand__name">Brookvale<br>Equipment Services</span>
    </div>
  </section>
</body>
</html>
```